Creative Businesss Card desgin!

Create a business card for our business Glint window cleaning!
We are open to creative ideas as long as it maintains a professional image.

Target Market(s)

Small Commercial window cleaning clients including car dealerships, strata manager, cafe

Industry/Entity Type

Window Cleaning

Contact Information for Business Card

Darren Pilkey
General Manager
Glint Window Cleaning

darren@glintservices.com.au
pane-tidy-corner.com.au
Ph: 1800 GO GLINT
Mob: 0438 572 619

Colors
fbed22
0392cd

Requirements
Should not have
• Stock window cleaning/ squeegee graphics

```html
<!DOCTYPE html>
<html lang="en">
<head>
<meta charset="utf-8">
<title>Glint Window Cleaning – Business Card</title>
<link rel="stylesheet" href="https://fonts.googleapis.com/css2?family=Roboto:wght@400;700;900&family=Roboto+Condensed:wght@700&family=Open+Sans:wght@400;700&display=swap">
<style>
  :root{
    --stage:#3a3a3a;
    --brand-blue:#1a5a88;
    --brand-blue-deep:#0c4a75;
    --brand-blue-light:#2f6f9e;
    --brand-yellow:#f2ea1f;
    --ink:#3f6f96;
    --ink-muted:#5b7f9c;
    --link:#12477a;
    --card-white:#ffffff;
  }
  *{box-sizing:border-box;margin:0;padding:0}
  html,body{width:1200px;height:900px;overflow:hidden}
  body{background:var(--stage);position:relative;font-family:"Open Sans",sans-serif}

  .card{position:absolute;width:520px;height:300px;border-radius:28px;overflow:hidden;box-shadow:0 18px 40px rgba(0,0,0,.45)}

  /* back side */
  .card--back{left:50px;top:300px;background:linear-gradient(160deg,var(--brand-blue-deep) 0%,var(--brand-blue) 55%,var(--brand-blue-light) 100%);display:flex;align-items:center;justify-content:center}
  .back-wordmark{font-family:"Roboto",sans-serif;font-weight:900;color:var(--brand-yellow);text-align:center;line-height:1}
  .back-wordmark .wordmark-name{display:block;font-size:72px;letter-spacing:2px}
  .back-wordmark .wordmark-tag{display:block;font-size:25px;margin-top:6px}

  /* front side */
  .card--front{left:630px;top:300px;background:var(--card-white)}
  .edge-tab{position:absolute;left:0;top:105px;width:10px;height:46px;background:var(--brand-yellow);border-radius:0 6px 6px 0}
  .front-wordmark{position:absolute;left:36px;top:26px;font-family:"Roboto",sans-serif;font-weight:900;color:var(--ink);line-height:1}
  .front-wordmark .wordmark-name{display:block;font-size:58px;letter-spacing:2px}
  .front-wordmark .wordmark-tag{display:block;font-size:20px;margin-top:4px}

  .person{position:absolute;left:42px;top:126px}
  .person-name{font-family:"Roboto Condensed",sans-serif;font-weight:700;font-size:21px;color:var(--ink);letter-spacing:.3px}
  .person-role{font-family:"Roboto",sans-serif;font-size:15px;color:var(--ink-muted);margin-top:2px}

  .contacts{position:absolute;left:34px;top:196px;list-style:none}
  .contacts li{display:flex;align-items:center;gap:8px;font-size:14px;color:var(--ink);height:21px}
  .contacts svg{width:14px;height:14px;flex:none;fill:var(--ink)}
  .contacts .web{font-weight:700;color:var(--link)}

  .accent-disc{position:absolute;right:-40px;top:70px;width:220px;height:220px;border-radius:50%;background:linear-gradient(160deg,#f5ee5c,var(--brand-yellow))}
</style>
</head>
<body>

<section class="card card--back" aria-label="Business card back">
  <div class="back-wordmark">
    <span class="wordmark-name">GLINT</span>
    <span class="wordmark-tag">WINDOW CLEANING</span>
  </div>
</section>

<section class="card card--front" aria-label="Business card front">
  <div class="edge-tab"></div>
  <div class="front-wordmark">
    <span class="wordmark-name">GLINT</span>
    <span class="wordmark-tag">WINDOW CLEANING</span>
  </div>

  <div class="person">
    <p class="person-name">DARREN PILKEY</p>
    <p class="person-role">General Manager</p>
  </div>

  <ul class="contacts">
    <li><svg viewBox="0 0 24 24"><path d="M6.6 10.8a15.1 15.1 0 0 0 6.6 6.6l2.2-2.2c.3-.3.7-.4 1-.2 1.1.4 2.3.6 3.6.6.6 0 1 .4 1 1V20c0 .6-.4 1-1 1A17 17 0 0 1 3 4c0-.6.4-1 1-1h3.5c.6 0 1 .4 1 1 0 1.3.2 2.5.6 3.6.1.3 0 .7-.2 1z"/></svg>1800 GO GLINT</li>
    <li><svg viewBox="0 0 24 24"><path d="M7 1h10a2 2 0 0 1 2 2v18a2 2 0 0 1-2 2H7a2 2 0 0 1-2-2V3a2 2 0 0 1 2-2zm0 3v14h10V4z"/></svg>0438 572 619</li>
    <li><svg viewBox="0 0 24 24"><path d="M2 5h20v14H2zm2 2v.5l8 5 8-5V7zm0 3v7h16v-7l-8 5z"/></svg>darren@glintservices.com.au</li>
    <li class="web"><svg viewBox="0 0 24 24"><path d="M12 2a10 10 0 1 0 0 20 10 10 0 0 0 0-20zm6.9 6h-3a15 15 0 0 0-1.3-3.9A8 8 0 0 1 18.9 8zM12 4c.8 1.1 1.5 2.5 1.9 4h-3.8c.4-1.5 1.1-2.9 1.9-4zM4.3 14a8 8 0 0 1 0-4h3.4a16 16 0 0 0 0 4zm.8 2h3a15 15 0 0 0 1.3 3.9A8 8 0 0 1 5.1 16zm3-8h-3a8 8 0 0 1 4.3-3.9A15 15 0 0 0 8.1 8zM12 20c-.8-1.1-1.5-2.5-1.9-4h3.8c-.4 1.5-1.1 2.9-1.9 4zm2.3-6H9.7a14 14 0 0 1 0-4h4.6a14 14 0 0 1 0 4zm.3 5.9a15 15 0 0 0 1.3-3.9h3a8 8 0 0 1-4.3 3.9zm1.7-5.9a16 16 0 0 0 0-4h3.4a8 8 0 0 1 0 4z"/></svg>pane-tidy-corner.com.au</li>
  </ul>

  <div class="accent-disc"></div>
</section>

</body>
</html>
```